Clothing Brand E-Commerce Website Design

We would like you to provide an ecommerce design template in layered PSD for our clothing/fashion brand website called "TrelWick".
We want the site to have a simple but sleek design similar to the following sites:
http://www.pivorane.com/
http://corvatelle.com/
http://www.dulvenor.com/
We want it to look stunning and blow the example sites out of the water. For color scheme, please use your imagination and try to impress us with your creativity.
We like teal and beige pink, with teal dominant.
Teal #7AFFFF / #46C6C6
Beige/pink #FF7B7C / #C74646
We want you to develop the design for 3 pages:
1) Home Page
Samples:
http://www.pivorane.com/
http://corvatelle.com/
http://www.dulvenor.com/
2) Products List Page (e.g., lists all "Dresses" when category is selected)
http://www.pivorane.com/shop/casual-dresses
http://www.dulvenor.com/index.php?main_page=index&cPath=3
http://corvatelle.com/modest-dresses.html
http://www.quillmarsh.com/Product/Category.aspx?br=q47&category=dress_maxi
3) Product Detail Page (e.g., individual product page with "Add to Cart")
http://www.pivorane.com/shop/dresses/lumen-fern-dress
http://corvatelle.com/modest-dresses/modest-dress-tova.html
http://www.dulvenor.com/index.php?main_page=product_info&cPath=3&products_id=297
Industry/Entity Type
Fashion

```html
<!DOCTYPE html>
<html lang="en">
<head>
<meta charset="utf-8">
<title>TrelWick – Home</title>
<link rel="stylesheet" href="https://fonts.googleapis.com/css2?family=Lato:ital,wght@0,300;0,400;0,700;1,400&family=Oswald:wght@500&display=swap">
<style>
:root{
  --page:#ebebeb;
  --foot:#dcfefe;
  --band:#5fd8d8;
  --teal:#46c6c6;
  --teal-dark:#3aa9a9;
  --pink:#ff7b7c;
  --ink:#222;
  --muted:#666;
  --line:#bfbfbf;
  --soft:#e3e3e3;
  --link:#3a9fd0;
}
*{box-sizing:border-box;margin:0;padding:0}
html,body{width:1200px;height:1098px;overflow:hidden}
body{position:relative;background:var(--page);font-family:"Lato",sans-serif;color:var(--ink)}
.abs{position:absolute}
.banner{position:absolute;top:26px;width:355px;height:194px;border:2px solid #fff}
.banner-spring{left:50px;background:linear-gradient(180deg,#7fb6dc 0%,#bcd3de 45%,#c78aa0 75%,#6d7d4c 100%)}
.banner-sale{left:424px;background:linear-gradient(90deg,#e9dccb 0%,#e4d4c1 55%,#c99aa6 78%,#eee6dd 100%)}
.banner-new{left:797px;background:linear-gradient(90deg,#caa06c 0%,#b98a57 40%,#d9283c 62%,#d9263a 100%)}
.sale-copy{position:absolute;left:34px;top:32px;font-family:"Oswald",sans-serif;color:#2b2b2b;line-height:1}
.sale-copy .small{font-size:24px;display:block}
.sale-copy .big{font-size:78px;display:block;margin-top:4px}
.section-title{left:50px;top:252px;font-size:22px;color:var(--teal);font-weight:400}
.arrow{position:absolute;top:258px;width:18px;height:18px}
.arrow-prev{left:1101px;background:var(--teal)}
.arrow-next{left:1132px;background:var(--pink)}
.rule{left:50px;top:288px;width:1101px;height:5px;border-top:1px solid var(--line);border-bottom:1px solid var(--line)}
.card{position:absolute;top:329px;width:264px;height:435px;background:#fff;border:1px solid #dedede}
.card .photo{position:absolute;left:20px;top:19px;width:225px;height:299px;border:1px solid #e4e4e4}
.card .ribbon{position:absolute;left:-5px;top:-4px}
.card .name{position:absolute;left:21px;top:329px;font-size:13px;color:#333}
.card .price{position:absolute;left:21px;top:351px;font-size:14px;color:var(--pink)}
.card .cart{position:absolute;left:20px;top:378px;width:135px;height:35px;background:var(--teal);color:#fff;font-size:16px;line-height:35px;text-align:center;text-transform:uppercase}
.card .cart.is-active{background:var(--pink)}
.card .icon-btn{position:absolute;top:378px;width:34px;height:35px;background:var(--soft)}
.card .compare{left:165px}.card .wish{left:209px}
.card .icon-btn svg{position:absolute;left:9px;top:10px}
.foot-band{left:0;top:850px;width:1200px;height:127px;background:var(--band)}
.foot{left:0;top:798px;width:1200px;height:300px;background:var(--foot)}
.about-panel{left:50px;top:838px}
.about-label{left:50px;top:860px;width:290px;text-align:center;color:#fff;font-size:19px;font-weight:300}
.brand{left:50px;top:905px;width:290px;text-align:center;color:#fff;font-size:44px;font-weight:700;letter-spacing:1px}
.foot-head{top:902px;color:#fff;font-size:20px;font-weight:400;text-transform:uppercase}
.like{left:1101px;top:903px;width:22px;height:22px;border-radius:50%;background:var(--teal-dark)}
.like-text{left:1128px;top:908px;font-size:9px;color:#fff}
.about-text{left:52px;top:1038px;width:280px;font-size:15px;line-height:25px}
.contact{left:404px;top:1032px;font-size:15px;line-height:30px}
.contact dt{display:inline-block;width:72px;font-size:16px}
.tweet-bird{left:672px;top:1040px;width:22px;height:18px;border-radius:50%;background:#333}
.tweet{left:703px;top:1035px;width:200px;font-size:12px;line-height:18px;color:var(--muted)}
.tweet a{color:var(--link);text-decoration:none;display:block}
.tweet em{display:block;color:var(--muted)}
.fans{left:977px;top:1036px;font-size:11px;color:#222}
.fans b{color:var(--pink);font-weight:400}
.avatar{position:absolute;top:1058px;width:32px;height:32px;background:#b2b2b2;border:2px solid #fff;box-shadow:0 0 1px #999}
.avatar span{position:absolute;top:34px;left:0;width:32px;text-align:center;font-size:7px;color:#333}
</style>
</head>
<body>

<div class="banner banner-spring" role="img" aria-label="Spring/Summer 2014 campaign photo: woman in a sun hat by a river with a city skyline, script lettering"></div>
<div class="banner banner-sale" role="img" aria-label="Sale photo: woman in a pink rain jacket against a wooden wall">
  <div class="sale-copy"><span class="small">Up to 60% Off</span><span class="big">Sale</span></div>
</div>
<div class="banner banner-new" role="img" aria-label="New Arrivals photo: woman in leopard print holding a handbag on red, script lettering"></div>

<h2 class="abs section-title">Special Products</h2>
<div class="arrow arrow-prev"><svg width="18" height="18"><path d="M10.5 5 6.5 9l4 4" fill="none" stroke="#fff" stroke-width="1.3"/></svg></div>
<div class="arrow arrow-next"><svg width="18" height="18"><path d="M7.5 5l4 4-4 4" fill="none" stroke="#fff" stroke-width="1.3"/></svg></div>
<div class="abs rule"></div>

<!-- product cards -->
<div class="card" style="left:50px">
  <div class="photo" role="img" aria-label="Product photo: knitted striped wrap cardigan" style="background:radial-gradient(ellipse at center,#b8917a 0%,#c9a895 35%,#fff 62%)"></div>
  <svg class="ribbon" width="135" height="105"><polygon points="0,68 0,100 130,0 83,0" fill="#8e5ba6"/><polygon points="0,100 4,104 4,97" fill="#5b3a6b"/><text x="0" y="0" transform="translate(26 72) rotate(-38)" fill="#fff" font-family="Lato" font-size="19">SALE</text></svg>
  <p class="name">Lorem ipsum dolor sit amet</p><p class="price">$ 175.00</p>
  <div class="cart is-active">Add to cart</div>
  <div class="icon-btn compare"><svg width="16" height="16"><rect x="1" y="3" width="11" height="11" fill="none" stroke="#ff7b7c" stroke-width="1.4"/><path d="M4 8l3 3 7-9" fill="none" stroke="#ff7b7c" stroke-width="1.4"/></svg></div>
  <div class="icon-btn wish"><svg width="16" height="16"><path d="M8 14 2 8a3.2 3.2 0 0 1 6-3 3.2 3.2 0 0 1 6 3z" fill="#ff7b7c"/></svg></div>
</div>

<div class="card" style="left:329px">
  <div class="photo" role="img" aria-label="Product photo: black parka with fur-trimmed hood" style="background:radial-gradient(ellipse at center,#1c1c1c 0%,#2a2a2a 38%,#fff 60%)"></div>
  <svg class="ribbon" width="135" height="105"><polygon points="0,68 0,100 130,0 83,0" fill="#2f8aa0"/><polygon points="0,100 4,104 4,97" fill="#1d5a68"/><text x="0" y="0" transform="translate(17 78) rotate(-38)" fill="#fff" font-family="Lato" font-size="19">-20% OFF</text></svg>
  <p class="name">Lorem ipsum dolor sit amet</p><p class="price">$ 175.00</p>
  <div class="cart">Add to cart</div>
  <div class="icon-btn compare"><svg width="16" height="16"><rect x="1" y="3" width="11" height="11" fill="none" stroke="#46c6c6" stroke-width="1.4"/><path d="M4 8l3 3 7-9" fill="none" stroke="#46c6c6" stroke-width="1.4"/></svg></div>
  <div class="icon-btn wish"><svg width="16" height="16"><path d="M8 14 2 8a3.2 3.2 0 0 1 6-3 3.2 3.2 0 0 1 6 3z" fill="#46c6c6"/></svg></div>
</div>

<div class="card" style="left:609px">
  <div class="photo" role="img" aria-label="Product photo: blue skinny jeans with ankle boots" style="background:radial-gradient(ellipse 30% 55% at center,#6f8ea8 0%,#9ab0c2 50%,#fff 100%)"></div>
  <svg class="ribbon" width="135" height="105"><polygon points="0,68 0,100 130,0 83,0" fill="#6aa84f"/><polygon points="0,100 4,104 4,97" fill="#436b31"/><text x="0" y="0" transform="translate(30 70) rotate(-38)" fill="#fff" font-family="Lato" font-size="19">NEW</text></svg>
  <p class="name">Lorem ipsum dolor sit amet</p><p class="price">$ 175.00</p>
  <div class="cart">Add to cart</div>
  <div class="icon-btn compare"><svg width="16" height="16"><rect x="1" y="3" width="11" height="11" fill="none" stroke="#46c6c6" stroke-width="1.4"/><path d="M4 8l3 3 7-9" fill="none" stroke="#46c6c6" stroke-width="1.4"/></svg></div>
  <div class="icon-btn wish"><svg width="16" height="16"><path d="M8 14 2 8a3.2 3.2 0 0 1 6-3 3.2 3.2 0 0 1 6 3z" fill="#46c6c6"/></svg></div>
</div>

<div class="card" style="left:888px">
  <div class="photo" role="img" aria-label="Product photo: sheer black shaping tights with heels on a grey backdrop" style="background:linear-gradient(180deg,#c8c8c8 0%,#dcdcdc 60%,#e8e8e8 100%)"></div>
  <svg class="ribbon" width="135" height="105"><polygon points="0,68 0,100 130,0 83,0" fill="#ec8a3c"/><polygon points="0,100 4,104 4,97" fill="#a85c22"/><text x="0" y="0" transform="translate(16 80) rotate(-38)" fill="#fff" font-family="Lato" font-size="19">HOT PRICE</text></svg>
  <p class="name">Lorem ipsum dolor sit amet</p><p class="price">$ 175.00</p>
  <div class="cart">Add to cart</div>
  <div class="icon-btn compare"><svg width="16" height="16"><rect x="1" y="3" width="11" height="11" fill="none" stroke="#46c6c6" stroke-width="1.4"/><path d="M4 8l3 3 7-9" fill="none" stroke="#46c6c6" stroke-width="1.4"/></svg></div>
  <div class="icon-btn wish"><svg width="16" height="16"><path d="M8 14 2 8a3.2 3.2 0 0 1 6-3 3.2 3.2 0 0 1 6 3z" fill="#46c6c6"/></svg></div>
</div>

<!-- footer -->
<div class="abs foot"></div>
<div class="abs foot-band"></div>
<svg class="abs about-panel" width="312" height="194">
  <path d="M290 0h10a10 10 0 0 1 10 10v2h-20z" fill="#2a9898"/>
  <path d="M10 0h280v150L145 192 0 150V10A10 10 0 0 1 10 0z" fill="#44c4c4"/>
</svg>
<div class="abs about-label">About</div>
<div class="abs brand">TrelWick</div>

<h3 class="abs foot-head" style="left:403px">Contact us</h3>
<h3 class="abs foot-head" style="left:680px">Latest tweets</h3>
<h3 class="abs foot-head" style="left:977px">Palmfeed</h3>
<div class="abs like"></div><div class="abs like-text">Like!</div>

<p class="abs about-text">Lorem ipsum dolor sit amet, conse adipiscing elit. Aenean eu porttitor eros. Suspendisse placerat semper vestibulum.</p>

<dl class="abs contact">
  <dd>Lorem ipsum dolor sit amet</dd>
  <dd><dt>Phone:</dt>1 - 234 - 567 - 89</dd>
  <dd><dt>Fax:</dt>1 - 234 - 567 - 89</dd>
</dl>

<div class="abs tweet-bird"></div>
<div class="abs tweet">Lorem ipsum dolor sit amet, adipiscing elit, sed diam nonummy <a>http://shrt.lk/trg87z</a><em>24 minutes ago</em></div>

<p class="abs fans">2450 people like <b>TrelWick</b></p>
<div class="avatar" style="left:975px"><span>Smith</span></div>
<div class="avatar" style="left:1023px"><span>John</span></div>
<div class="avatar" style="left:1072px"><span>Jane</span></div>
<div class="avatar" style="left:1120px"><span>Mary</span></div>

</body>
</html>
```